Project Sign for Construction Company

Site contractor needs a 4'x8' sign to place on construction sites for advertising. Our company builds the infrastructure for new housing developments. These sign will be posted on the road side to be viewed by passing cars. I want a clean and bold look and feel that resembles my company logo.

Font styles to use
Other font styles liked:
• Hypatia Sans Pro

Colors

Designer to choose colors to be used in the design.

Requirements
Must have
• 555-382-9146 | Info@MarlowPaving.example
• CUC 8047319
• www.MarlowPaving.example
• Services
• Road Construction
• Site Preparation & Excavation
• Underground Utilities
• Shoreline Restoration
Nice to have
• Now Hiring
• Pipe Layers
• Foremen
• Equipment Operators
Should not have
• Should not have stock picture images used in the design, focus on logo and geometric shapes

```html
<!DOCTYPE html>
<html lang="en">
<head>
<meta charset="utf-8">
<title>Marlow Paving – Site Sign</title>
<link rel="stylesheet" href="https://fonts.googleapis.com/css2?family=Cabin:wght@500;600;700&display=swap">
<style>
  :root {
    --page: #eeeeec;
    --white: #ffffff;
    --brand-blue: #1b4f9c;
    --band-grey: #6d6d6d;
    --band-black: #050505;
    --silver-light: #f4f4f4;
    --silver-dark: #b9b9b9;
    --ink: #111111;
    --photo-paper: #f1f3f6;
    --photo-blueprint: #d3dae4;
    --photo-amber: #e6cf94;
  }
  * { margin: 0; padding: 0; box-sizing: border-box; }
  html, body {
    width: 744px; height: 1200px; overflow: hidden;
    background: var(--page);
    font-family: "Cabin", sans-serif;
  }
  .sign {
    position: absolute; left: 20px; top: 424px;
    width: 704px; height: 352px;
    background: var(--white);
    box-shadow: 0 6px 18px rgba(0,0,0,.18);
    overflow: hidden;
  }
  .sign-shapes { position: absolute; inset: 0; }
  .brand-name {
    position: absolute; right: 32px; top: 84px;
    font-weight: 700; font-size: 30px; color: var(--brand-blue);
    letter-spacing: .5px; display: flex; align-items: center; gap: 10px;
  }
  .brand-mark { width: 14px; height: 14px; background: var(--brand-blue); }
  .services-title {
    position: absolute; right: 30px; top: 142px;
    font-weight: 700; font-size: 26px; color: var(--white); letter-spacing: .5px;
  }
  .service-list {
    position: absolute; right: 28px; top: 180px;
    list-style: none; text-align: right;
  }
  .service-list li {
    font-weight: 600; font-size: 14px; color: var(--white);
    height: 23.5px; line-height: 23.5px;
  }
  .service-list li::after { content: "•"; margin-left: 10px; }
  .hiring-line {
    position: absolute; right: 30px; top: 282px;
    font-weight: 600; font-size: 11px; color: var(--white);
  }
  .contact-phone {
    position: absolute; left: 316px; top: 314px;
    display: flex; align-items: center; gap: 5px;
    font-weight: 700; font-size: 19px; color: var(--white); letter-spacing: .5px;
  }
  .contact-divider {
    position: absolute; left: 468px; top: 315px;
    width: 1px; height: 26px; background: var(--white);
  }
  .contact-web {
    position: absolute; left: 476px; top: 316px;
    font-weight: 600; font-size: 9px; color: var(--white); line-height: 12px;
  }
  .contact-web span { display: flex; align-items: center; gap: 3px; }
  .contact-web span::before {
    content: ""; width: 4px; height: 4px; background: var(--white);
  }
  .licence {
    position: absolute; right: 8px; top: 332px;
    font-weight: 700; font-size: 9.5px; color: var(--ink);
  }
</style>
</head>
<body>
  <main class="sign">
    <svg class="sign-shapes" width="704" height="352" viewBox="0 0 704 352">
      <defs>
        <linearGradient id="photoTone" x1="0" y1="0" x2="1" y2="1">
          <stop offset="0" stop-color="var(--photo-paper)"/>
          <stop offset=".55" stop-color="var(--photo-blueprint)"/>
          <stop offset="1" stop-color="var(--photo-amber)"/>
        </linearGradient>
        <linearGradient id="silver" x1="0" y1="0" x2="1" y2="0">
          <stop offset="0" stop-color="var(--silver-dark)"/>
          <stop offset=".5" stop-color="var(--silver-light)"/>
          <stop offset="1" stop-color="var(--silver-dark)"/>
        </linearGradient>
      </defs>
      <polygon role="img" aria-label="Desk photo with architectural blueprints, pencils, protractor, notebook and keyboard"
               points="0,0 457,0 273,352 0,352" fill="url(#photoTone)"/>
      <polygon class="services-panel" points="440,137 704,137 704,278 374,278" fill="var(--brand-blue)"/>
      <polygon class="hiring-band" points="342,278 704,278 704,301 330,301" fill="var(--band-grey)"/>
      <polygon class="contact-band" points="299,301 704,301 704,352 273,352" fill="var(--band-black)"/>
      <polygon class="licence-badge" points="617,322 704,316 704,352 609,352" fill="url(#silver)"/>
    </svg>

    <div class="brand-name"><span class="brand-mark"></span>Marlow Paving</div>

    <h2 class="services-title">SERVICES</h2>
    <ul class="service-list">
      <li>Road Construction</li>
      <li>Site Preparation &amp; Excavation</li>
      <li>Underground Utilities</li>
      <li>Shoreline Restoration</li>
    </ul>

    <p class="hiring-line">Now Hiring | Pipe Layers | Foremen | Equipment Operators</p>

    <p class="contact-phone">
      <svg width="16" height="16" viewBox="0 0 16 16" aria-hidden="true">
        <circle cx="8" cy="8" r="7" fill="none" stroke="#fff" stroke-width="1.4"/>
        <path d="M5.6 4.4l1.4 1.6-.7 1a5 5 0 0 0 2.7 2.7l1-.7 1.6 1.4-.9 1.1C8.2 11.4 4.6 7.8 4.5 5.3z" fill="#fff"/>
      </svg>
      555-382-9146
    </p>
    <div class="contact-divider"></div>
    <p class="contact-web">
      <span>Info@MarlowPaving.example</span>
      <span>www.MarlowPaving.example</span>
    </p>

    <p class="licence">CUC 8047319</p>
  </main>
</body>
</html>
```